Skipper and fishing guide brochure

logo and brochure. Please see the word doc tobi 2 for brochure style. Please give me something unique and clean, not you typical fishing/boating logo. Tobias is a fishing guide and boat skipper. He moves some very expensive boats and helps people enjoy their very expensive toys. he works for people who have lots of money, toys and little time.

Target Market(s)

boat owners/buyers/boat sellers

Logo Text

Tobias Merlane

Requirements
Nice to have
• logo will be embroided on shirts and hats, would be nice to have some alternate colourways. EG on white, on grey and on black
Should not have
• trashy style font

```html
<!DOCTYPE html>
<html lang="en">
<head>
<meta charset="utf-8">
<title>Tobias Merlane – Skipper &amp; Fishing Guide Brochure</title>
<link rel="stylesheet" href="https://fonts.googleapis.com/css2?family=Anton&family=Bebas+Neue&family=Montserrat:wght@400;500;600;700&display=swap">
<style>
:root{
  --board:#4b4b4b;
  --paper:#ffffff;
  --ink:#3e4448;
  --body:#2f3336;
  --teal:#3f8f96;
  --blue:#3f8fc9;
  --slate:#6d7f8d;
  --sky:#86c6d6;
  --mist:#a3bcc2;
  --ghost:#f2f3f4;
  --placeholder:#c9d5d6;
  --label:#c4c4c4;
  --rule:#d5dadc;
  --cover-first:#66625a;
  --cover-last:#7d7a72;
}
*{box-sizing:border-box;margin:0;padding:0}
html,body{width:1200px;height:2296px;overflow:hidden;background:var(--board)}
body{font-family:"Montserrat",sans-serif;color:var(--body)}
.board{position:relative;width:1200px;height:2296px;background:var(--board)}

.spread{position:absolute;left:112px;width:944px;height:670px;background:var(--paper);overflow:hidden;box-shadow:0 6px 18px rgba(0,0,0,.45)}
.spread--outside{top:73px}
.spread--inside-1{top:800px}
.spread--inside-2{top:1538px}
.fold{position:absolute;top:0;left:472px;width:60px;height:100%;background:linear-gradient(90deg,rgba(0,0,0,.06),rgba(0,0,0,0));pointer-events:none;z-index:5}
.fold::before{content:"";position:absolute;top:0;right:60px;width:40px;height:100%;background:linear-gradient(270deg,rgba(0,0,0,.04),rgba(0,0,0,0))}

.spread-label{position:absolute;left:1102px;width:300px;font-weight:500;font-size:34px;letter-spacing:3px;color:var(--label);transform:rotate(-90deg);transform-origin:top left;white-space:nowrap}

.photo{position:absolute}
.ghost-name{position:absolute;font-family:"Anton",sans-serif;color:var(--ghost);line-height:.86;white-space:nowrap;text-transform:uppercase;z-index:0}

.logo-placeholder{position:absolute;text-align:center;color:var(--placeholder);font-family:"Bebas Neue",sans-serif;line-height:1;z-index:2}
.logo-placeholder .logo-word{display:block}
.logo-placeholder .logo-sub{display:block;font-family:"Montserrat",sans-serif;font-weight:500;letter-spacing:2px}

/* outside */
.services{position:absolute;left:0;top:36px;width:472px;text-align:center;z-index:2}
.services-title{font-weight:600;font-size:17px;letter-spacing:.5px;color:var(--ink)}
.services-title span{color:var(--teal)}
.service-list{list-style:none;margin-top:16px;display:flex;flex-direction:column;align-items:center;gap:6px}
.service-list li{font-size:10px;color:var(--body);border:1px solid #b9c6c9;border-radius:10px;padding:3px 0;width:228px;background:var(--paper)}
.service-list li.narrow{width:170px}
.service-list li.short{width:120px}
.services-note{margin-top:28px;font-size:10px;line-height:15px;color:var(--body)}

.contact{position:absolute;left:0;top:552px;width:472px;text-align:center;font-size:9px;line-height:11px;color:var(--body);z-index:2}
.contact-title{font-weight:700;color:var(--teal);font-size:9.5px;letter-spacing:.5px}
.contact-title span{color:var(--ink);font-weight:600}
.contact-icons{display:flex;justify-content:center;gap:6px;margin:7px 0 6px}
.contact-icons svg{width:11px;height:11px}
.contact-name{font-weight:700;color:var(--teal);font-size:9.5px}

.cover-name{position:absolute;left:494px;top:578px;width:420px;transform:rotate(-90deg);transform-origin:top left;font-family:"Anton",sans-serif;font-weight:400;text-transform:uppercase;white-space:nowrap;z-index:3}
.cover-name .first{display:block;font-size:148px;line-height:128px;color:var(--cover-first)}
.cover-name .last{display:block;font-size:120px;line-height:104px;color:var(--cover-last)}
.cover-site{position:absolute;left:508px;top:612px;font-size:11px;letter-spacing:3.2px;font-weight:500;color:var(--ink);z-index:3}

/* inside copy */
.copy{position:absolute;font-size:8.4px;line-height:12.4px;color:var(--body);text-align:justify;z-index:2}
.copy p+p{margin-top:12.4px}

.talk-head{position:absolute;z-index:2}
.talk-head::before{content:"";position:absolute;left:-10px;top:3px;width:3px;height:18px;background:var(--blue)}
.talk-head .kicker{display:block;font-weight:700;font-size:19px;line-height:20px;color:var(--blue);letter-spacing:.3px}
.talk-head .topic{display:block;font-weight:700;font-size:34px;line-height:36px;color:#a8b2b7;letter-spacing:.5px}

.motto{position:absolute;left:500px;top:26px;width:410px;height:252px;border:1px solid var(--rule);border-left:none;z-index:2}
.motto-line{position:absolute;right:8px;font-family:"Bebas Neue",sans-serif;line-height:.8;white-space:nowrap}
.motto-patience{top:14px;font-size:104px;color:var(--slate)}
.motto-persistence{top:96px;font-size:97px;color:var(--sky)}
.motto-perfection{top:174px;font-size:96px;color:var(--mist)}
.motto-and{position:absolute;left:10px;top:248px;font-family:"Bebas Neue",sans-serif;font-size:54px;line-height:.8;color:#8d9499;transform:rotate(-90deg);transform-origin:top left;letter-spacing:1px}

.small-head{position:absolute;font-weight:700;font-size:15px;color:var(--blue);letter-spacing:.3px;z-index:2}
.small-head::before{content:"";position:absolute;left:-9px;top:2px;width:3px;height:14px;background:var(--blue)}

.footer-site{position:absolute;top:632px;font-size:9px;letter-spacing:1.6px;color:var(--ink);z-index:2}
.footer-social{position:absolute;top:630px;font-size:9px;color:var(--ink);display:flex;align-items:center;gap:4px;z-index:2}
.footer-social i{display:inline-block;width:9px;height:9px;border-radius:50%;background:#8e9aa0}
.footer-rule{position:absolute;top:638px;height:1px;background:var(--rule);z-index:2}

/* inside 2 */
.overlay-name{position:absolute;left:6px;top:545px;width:450px;transform:rotate(-90deg);transform-origin:top left;font-family:"Anton",sans-serif;font-weight:400;color:rgba(255,255,255,.72);text-transform:uppercase;white-space:nowrap;z-index:3}
.overlay-name .first{display:block;font-size:118px;line-height:102px}
.overlay-name .last{display:block;font-size:134px;line-height:116px}
</style>
</head>
<body>
<main class="board">

  <!-- OUTSIDE -->
  <section class="spread spread--outside" aria-label="Outside spread">
    <div class="ghost-name" style="left:0;top:690px;font-size:90px;transform:rotate(-90deg);transform-origin:top left">Tobias<br>Merlane</div>
    <div class="ghost-name" style="left:150px;top:400px;font-size:80px">Tobias<br>Merlane</div>

    <div class="services">
      <h2 class="services-title">SERVICES <span>OFFERED</span></h2>
      <ul class="service-list">
        <li>Guided fishing from your own boat</li>
        <li>Skippering for game fishing competitions</li>
        <li>Pleasure cruises/power boat day skipper</li>
        <li class="narrow">Boat Relocations</li>
        <li class="narrow">On water vessel delivery</li>
        <li class="short">Provisioning</li>
      </ul>
      <p class="services-note">I am available to help you plan out your perfect day on the water,<br>just let me know what your dreaming up.</p>
    </div>

    <div class="logo-placeholder" style="left:162px;top:324px;width:146px;height:146px;border:2px solid var(--placeholder);padding-top:34px;background:rgba(255,255,255,.6)">
      <span class="logo-word" style="font-size:54px">LOGO</span>
      <span class="logo-sub" style="font-size:14px;margin-top:4px">GOES HERE</span>
    </div>

    <div class="contact">
      <p class="contact-title">GET IN TOUCH <span>WITH ME</span></p>
      <div class="contact-icons">
        <svg viewBox="0 0 12 12" aria-hidden="true"><circle cx="6" cy="6" r="6" fill="#3f8f96"/><path d="M4 3.2l1 1.2-.6.8c.4.8 1 1.4 1.8 1.8l.8-.6 1.2 1-.5 1c-2.3-.3-4-2-4.3-4.3z" fill="#fff"/></svg>
        <svg viewBox="0 0 12 12" aria-hidden="true"><circle cx="6" cy="6" r="6" fill="#3f8f96"/><rect x="3" y="4" width="6" height="4.2" fill="#fff"/><path d="M3 4l3 2.3L9 4" stroke="#3f8f96" stroke-width=".7" fill="none"/></svg>
        <svg viewBox="0 0 12 12" aria-hidden="true"><circle cx="6" cy="6" r="6" fill="#3f8f96"/></svg>
      </div>
      <p class="contact-name">TOBIAS MERLANE</p>
      <p>0412 557 308</p>
      <p>tmerlane@harbourmail.com</p>
      <p>https://www.socialsite.com/tobiasmerlane/</p>
    </div>

    <div class="photo" role="img" aria-label="Photo of the skipper on coastal rocks holding up a large fish, ocean and headland behind" style="left:722px;top:0;width:222px;height:670px;border-top-left-radius:26px;background:linear-gradient(180deg,#8fc3e6 0%,#b7d9ec 22%,#5e8a6a 32%,#3f8ea3 50%,#d8ecef 62%,#7b6a5e 80%,#4b3f39 100%)"></div>

    <div class="logo-placeholder" style="left:540px;top:42px;width:110px">
      <span class="logo-word" style="font-size:56px">LOGO</span>
      <span class="logo-sub" style="font-size:13px;margin-top:4px">GOES HERE</span>
    </div>

    <h1 class="cover-name"><span class="first">Tobias</span><span class="last">Merlane</span></h1>
    <p class="cover-site">WWW.YOURWEBSITE.COM</p>
    <div class="fold"></div>
  </section>
  <p class="spread-label" style="top:744px">OUTSIDE</p>

  <!-- INSIDE 1 -->
  <section class="spread spread--inside-1" aria-label="Inside spread one">
    <div class="ghost-name" style="left:30px;top:370px;font-size:80px">Tobias<br>Merlane</div>
    <div class="ghost-name" style="left:724px;top:470px;font-size:72px">Tobias<br>Merlane</div>

    <h2 class="talk-head" style="left:37px;top:28px"><span class="kicker">LET'S<br>TALK ABOUT</span><span class="topic">FISHING</span></h2>

    <div class="copy" style="left:30px;top:124px;width:224px">
      <p>With different species popping their heads in to different locations all year round, the crew and I can always find something to target. Setting off with a plan, we steam, search, and work as a team to do what we do best...Catch fish.</p>
      <p>Game fishing is a team sport, our crew mesh perfectly into a fish catching machine. We have been fortunate enough to be taught by some of the biggest names in fishing and have now gone forward to continue to lead the recreational scene with international records and consistent personal captures that blow most people's minds.</p>
      <p>Game fishing competitions are generally multi day events with great atmosphere. We can crew your vessel to location if needed, during event and back to base. If you're not already a member, entry into comps requires becoming a member of a club and fees normally start from $99pp. Only the angler needs to be a member of a GFSA affiliated club to enter your vessel in the running to possibly take out the win. For any further enquiries please call me on 0412 557 308.</p>
    </div>

    <div class="logo-placeholder" style="left:64px;top:520px;width:130px">
      <span class="logo-word" style="font-size:62px">LOGO</span>
      <span class="logo-sub" style="font-size:15px;margin-top:4px">GOES HERE</span>
    </div>

    <div class="photo" role="img" aria-label="Photo of the skipper on a boat deck leaning back while holding a big fish, open sea and bright sky behind" style="left:260px;top:0;width:414px;height:670px;background:linear-gradient(180deg,#e9f4fb 0%,#a9d2ec 25%,#2f7fb4 42%,#3a86b9 55%,#d9e4ea 68%,#2e68a8 82%,#3a4450 100%)"></div>

    <div class="motto" aria-label="Patience, persistence and perfection">
      <span class="motto-line motto-patience">PATIENCE</span>
      <span class="motto-line motto-persistence">PERSISTENCE</span>
      <span class="motto-line motto-perfection">PERFECTION</span>
      <span class="motto-and">AND</span>
    </div>

    <h3 class="small-head" style="left:712px;top:330px">CREW</h3>
    <div class="copy" style="left:701px;top:360px;width:212px">
      <p>Depending on vessel size depends on crew numbers but we normally like to run a 2-man crew for game fishing. Deck hand Adam Kestrell has an extensive and international game fishing history as well as pro and recreational fishing. Adam has been schooled up by one of the biggest names in east Australian game fishing, Ross Tallard as well as years under Russ Penwick in Vanuatu. Adam brings a wealth of fishing and boating knowledge to the crew.</p>
    </div>

    <p class="footer-site" style="left:37px">www.yourwebsite.com</p>
    <div class="footer-rule" style="left:170px;width:88px"></div>
    <div class="footer-rule" style="left:676px;width:54px"></div>
    <p class="footer-social" style="left:734px"><i></i>https://www.socialsite.com/tobiasmerlane/</p>
    <div class="fold"></div>
  </section>
  <p class="spread-label" style="top:1471px">INSIDE 1</p>

  <!-- INSIDE 2 -->
  <section class="spread spread--inside-2" aria-label="Inside spread two">
    <div class="ghost-name" style="left:40px;top:566px;font-size:60px;transform:scaleY(-1)">Tobias</div>
    <div class="ghost-name" style="left:700px;top:440px;font-size:80px">Tobias<br>Merlane</div>

    <div class="photo" role="img" aria-label="Photo of the skipper at the side of a boat holding a fish in clear blue water" style="left:0;top:76px;width:657px;height:480px;background:linear-gradient(160deg,#2b7fb0 0%,#3d98c6 35%,#6db8da 60%,#2f6fb0 80%,#2a4f8f 100%)"></div>

    <div class="overlay-name"><span class="first">Tobias</span><span class="last">Merlane</span></div>

    <div class="logo-placeholder" style="left:840px;top:24px;width:80px">
      <span class="logo-word" style="font-size:40px">LOGO</span>
      <span class="logo-sub" style="font-size:10px;margin-top:2px">GOES HERE</span>
    </div>

    <h3 class="small-head" style="left:712px;top:100px">ABOUT ME</h3>
    <div class="copy" style="left:701px;top:126px;width:216px">
      <p>Growing up in Victoria I cut my teeth on bread and butter species like most others but quickly pushed forward and explored the wonderful world of fishing. Relocating to the Sunshine Coast with the Noosa River and Sunshine Coast offshore as my playground, it gave me the perfect environment to continue to learn the art of catching fish. Mainly self-taught I love to push the boundaries, and have added some of Australia's finest captures to my name.</p>
      <p>Being completely fishing obsessed I have 4 year's experience guiding the Great Barrier Reef running 7 day live aboard charters offering a wide array of fishing types from heavy and light tackle game fishing, sport fishing right through to getting a feed of the tastiest fish the area has to offer.</p>
      <p>A universal angler and guide I have fished my way right around the coast of Australia and am always on the pulse with what's biting, where and when. With my extensive experience aboard much larger operations I always recommend a trip plan, and show organisation and communication skills to ensure a safe and pleasurable trip.</p>
    </div>

    <p class="footer-site" style="left:37px">www.yourwebsite.com</p>
    <div class="footer-rule" style="left:170px;width:500px"></div>
    <div class="footer-rule" style="left:676px;width:54px"></div>
    <p class="footer-social" style="left:734px"><i></i>https://www.socialsite.com/tobiasmerlane/</p>
    <div class="fold"></div>
  </section>
  <p class="spread-label" style="top:2208px">INSIDE 2</p>

</main>
</body>
</html>
```